Startup company business card (Media & Advertising)

we need a business card design for a company that is a startup in the media and aggregation industry. Card needs to look funky and of a new breed/modern and upmarket.

Target Market(s)

advertisers/ brand agencies & media publishers

Industry/Entity Type

Advertising

Contact Information for Business Card

Please ensure the front face signifies our brand (plumvexo.com) and back has details for the contact. Standard contact such as phone , address, email , website etc.

Font styles to use
Other font styles liked:
• use styleguide and logo font and color

Colors

Designer to choose colors to be used in the design.

Requirements
Must have
• We are disrupting the media and agency industry so subtlety would be good to use imagery to signify this
Nice to have
• Please use logo colors for branding
Should not have
• be as creative and provide few options. Pick a brand color from logo and styleguide

```html
<!DOCTYPE html>
<html lang="en">
<head>
<meta charset="utf-8">
<title>plumVexo business card</title>
<link rel="stylesheet" href="https://fonts.googleapis.com/css2?family=Arvo:wght@400;700&family=Nunito+Sans:wght@400;600&display=swap">
<style>
  :root {
    --stage: #1e1e1e;
    --ink: #111111;
    --card-dark: #0b0a0b;
    --pattern-tone: #1c0e12;
    --paper: #ffffff;
    --brand-red: #ee3a48;
    --brand-plum: #9c1a45;
    --text-light: #ffffff;
    --tagline: #f6d6da;
  }
  * { margin: 0; padding: 0; box-sizing: border-box; }
  html, body { width: 1200px; height: 900px; overflow: hidden; background: var(--stage); }
  .stage { position: relative; width: 1200px; height: 900px; }

  .card { position: absolute; left: 250px; width: 700px; height: 400px; overflow: hidden; }

  /* Front */
  .card-front { top: 40px; background: var(--card-dark); }
  .front-pattern {
    position: absolute; inset: 0 0 88px 0;
    background: radial-gradient(ellipse at 50% 45%, var(--pattern-tone), var(--card-dark) 75%);
  }
  .brand-lockup { position: absolute; display: flex; align-items: center; gap: 16px; }
  .front-lockup { left: 50%; top: 132px; transform: translateX(-50%); }
  .brand-dot { width: 34px; height: 34px; border-radius: 50%; background: var(--brand-red); }
  .brand-name { font-family: "Arvo", serif; font-weight: 700; font-size: 40px; letter-spacing: 1px; }
  .front-lockup .brand-name { color: var(--text-light); }
  .tagline-band {
    position: absolute; left: 0; right: 0; bottom: 0; height: 88px;
    background: linear-gradient(90deg, var(--brand-red) 0%, var(--brand-red) 35%, var(--brand-plum) 100%);
    display: flex; flex-direction: column; justify-content: center; align-items: center;
  }
  .tagline {
    font-family: "Arvo", serif; font-size: 14px; letter-spacing: 2.2px;
    text-transform: uppercase; color: var(--tagline); line-height: 1.45; text-align: center;
  }

  /* Back */
  .card-back { top: 460px; background: var(--paper); }
  .back-lockup { left: 410px; top: 40px; }
  .back-lockup .brand-name { color: var(--ink); }
  .back-lockup .brand-dot { width: 44px; height: 44px; }
  .contact-name { position: absolute; left: 372px; top: 118px; font-family: "Arvo", serif; font-size: 30px; color: var(--ink); }
  .contact-role { position: absolute; left: 372px; top: 156px; font-family: "Nunito Sans", sans-serif; font-size: 19px; color: #222; }
  .divider { position: absolute; left: 364px; right: 0; top: 196px; height: 2px; background: linear-gradient(90deg, var(--brand-red), var(--brand-plum)); }
  .contact-list { position: absolute; left: 372px; top: 214px; list-style: none; }
  .contact-list li {
    display: flex; align-items: center; gap: 12px; height: 27px;
    font-family: "Nunito Sans", sans-serif; font-size: 20px; color: var(--ink);
  }
  .contact-list svg { width: 18px; height: 18px; flex: none; }
  .address { position: absolute; left: 372px; top: 300px; font-family: "Nunito Sans", sans-serif; font-size: 20px; line-height: 1.25; color: var(--ink); }
  .corner-band { position: absolute; left: 0; bottom: 0; width: 700px; height: 40px; }
</style>
</head>
<body>
<main class="stage">
  <section class="card card-front" aria-label="Card front">
    <div class="front-pattern" role="img" aria-label="Faint repeating brand-mark pattern on black"></div>
    <div class="brand-lockup front-lockup">
      <span class="brand-dot"></span>
      <span class="brand-name">plumVexo</span>
    </div>
    <div class="tagline-band">
      <p class="tagline">We are disrupting the media and agency industry</p>
      <p class="tagline">so subtlety would be good to use imagery to signify this</p>
    </div>
  </section>

  <section class="card card-back" aria-label="Card back">
    <div class="brand-lockup back-lockup">
      <span class="brand-dot"></span>
      <span class="brand-name">plumVexo</span>
    </div>
    <h1 class="contact-name">Marco Delvane</h1>
    <p class="contact-role">CEO &amp; Founder</p>
    <div class="divider"></div>
    <ul class="contact-list">
      <li>
        <svg viewBox="0 0 20 20" fill="none" stroke="#e8344a" stroke-width="1.6"><circle cx="10" cy="10" r="8.2"/><path d="M7 6.2l1.5-.4 1 2.2-1 .9a5 5 0 0 0 2.6 2.6l.9-1 2.2 1-.4 1.5c-3.6.4-7.2-3.2-6.8-6.8z"/></svg>
        +34 611.205.938
      </li>
      <li>
        <svg viewBox="0 0 20 20" fill="none" stroke="#e8344a" stroke-width="1.6"><rect x="2" y="4.5" width="16" height="11"/><path d="M2 4.5l8 6.5 8-6.5"/></svg>
        delvane@plumvexo.com
      </li>
      <li>
        <svg viewBox="0 0 20 20" fill="none" stroke="#e8344a" stroke-width="1.6"><circle cx="10" cy="10" r="8"/><path d="M2 10h16M10 2c-3 3-3 13 0 16M10 2c3 3 3 13 0 16M3.5 6h13M3.5 14h13"/></svg>
        www.plumvexo.com
      </li>
    </ul>
    <p class="address">P.O. Box 4182 Halden<br>Wyoming 83017</p>
    <svg class="corner-band" viewBox="0 0 700 40" preserveAspectRatio="none" aria-hidden="true">
      <defs>
        <linearGradient id="bandGradient" x1="0" x2="1" y1="0" y2="0">
          <stop offset="0" stop-color="#ee3a48"/>
          <stop offset="1" stop-color="#9c1a45"/>
        </linearGradient>
      </defs>
      <polygon points="340,10 700,10 700,40 356,40" fill="url(#bandGradient)"/>
    </svg>
  </section>
</main>
</body>
</html>
```